Business Card Design Project

We're an orthopaedic office, and our colors are blue white and balck. Dealing with physicians and healthcare execs, I'd like this card to have a classy, yet overpowering wow factor.

Here are a couple of cards I like that are close to what I'm looking for:
http://www.plumvantia.com/design/671583
http://www.plumvantia.com/design/514515

```html
<!DOCTYPE html>
<html lang="en">
<head>
<meta charset="utf-8">
<title>Business Card Colour Options</title>
<link rel="stylesheet" href="https://fonts.googleapis.com/css2?family=PT+Sans&family=Arimo&display=swap">
<style>
  :root {
    --page: #ffffff;
    --frame: #3a3a3a;
    --card-face: #ffffff;
    --ink: #333333;
    --ink-soft: #3c3c3c;
    --brand-dot: #2b3990;
    --accent-red: #e8202a;
    --accent-yellow: #ffd200;
    --accent-teal: #58aab8;
    --accent-dark: #454040;
  }
  * { box-sizing: border-box; margin: 0; padding: 0; }
  html, body {
    width: 1200px; height: 901px; overflow: hidden; background: var(--page);
  }
  .sheet {
    position: relative; width: 1200px; height: 901px;
    border: 2px solid var(--frame);
  }
  .card {
    position: absolute; width: 427px; height: 261px;
    background: var(--accent);
  }
  .card--red { left: 144px; top: 147px; --accent: var(--accent-red); }
  .card--yellow { left: 629px; top: 147px; --accent: var(--accent-yellow); }
  .card--teal { left: 144px; top: 441px; --accent: var(--accent-teal); }
  .card--dark { left: 629px; top: 441px; --accent: var(--accent-dark); --title: var(--ink); }
  .card__face {
    position: absolute; left: 20px; top: 19px; width: 387px; height: 223px;
    background: var(--card-face); border-radius: 24px; overflow: hidden;
  }
  .brand {
    position: absolute; right: 21px; top: 12px;
    display: flex; align-items: center; gap: 5px;
    font-family: "PT Sans", sans-serif; font-weight: 400; color: var(--ink);
  }
  .brand__dot {
    width: 24px; height: 24px; border-radius: 50%; background: var(--brand-dot);
  }
  .brand__text { text-align: right; line-height: 1; }
  .brand__name { display: block; font-size: 19px; letter-spacing: 0.2px; }
  .brand__tag { display: block; font-size: 9.5px; margin-top: 1px; }
  .brand__sub { display: block; font-size: 5px; margin-top: 1px; }
  .holder {
    position: absolute; right: 17px; top: 86px;
    font-family: "PT Sans", sans-serif; font-size: 21.5px; color: var(--ink);
    white-space: nowrap;
  }
  .holder__title { color: var(--title, var(--accent)); }
  .divider {
    position: absolute; left: 0; right: 0; top: 115px; height: 1.5px;
    background: var(--accent);
  }
  .contact {
    position: absolute; left: 24px; top: 144px; list-style: none;
    font-family: "Arimo", sans-serif; font-size: 13px; color: var(--ink-soft);
    line-height: 21px;
  }
  .caption {
    position: absolute; left: 0; right: 0; top: 732px; text-align: center;
    font-family: "PT Sans", sans-serif; font-size: 19px; color: var(--ink);
  }
</style>
</head>
<body>
<main class="sheet">

  <section class="card card--red">
    <div class="card__face">
      <div class="brand">
        <span class="brand__dot"></span>
        <span class="brand__text">
          <span class="brand__name">CRESTLINE</span>
          <span class="brand__tag">Orthopaedic &amp; Sports</span>
          <span class="brand__sub">Medicine Center</span>
        </span>
      </div>
      <p class="holder">DORIAN WHITFIELD <span class="holder__title">[CEO]</span></p>
      <div class="divider"></div>
      <ul class="contact">
        <li>2180 Larkspur Ave., Fairmont, OR 97015</li>
        <li>dwhitfield@crestlineortho.com</li>
        <li>(555)318-2047</li>
      </ul>
    </div>
  </section>

  <section class="card card--yellow">
    <div class="card__face">
      <div class="brand">
        <span class="brand__dot"></span>
        <span class="brand__text">
          <span class="brand__name">CRESTLINE</span>
          <span class="brand__tag">Orthopaedic &amp; Sports</span>
          <span class="brand__sub">Medicine Center</span>
        </span>
      </div>
      <p class="holder">DORIAN WHITFIELD <span class="holder__title">[CEO]</span></p>
      <div class="divider"></div>
      <ul class="contact">
        <li>2180 Larkspur Ave., Fairmont, OR 97015</li>
        <li>dwhitfield@crestlineortho.com</li>
        <li>(555)318-2047</li>
      </ul>
    </div>
  </section>

  <section class="card card--teal">
    <div class="card__face">
      <div class="brand">
        <span class="brand__dot"></span>
        <span class="brand__text">
          <span class="brand__name">CRESTLINE</span>
          <span class="brand__tag">Orthopaedic &amp; Sports</span>
          <span class="brand__sub">Medicine Center</span>
        </span>
      </div>
      <p class="holder">DORIAN WHITFIELD <span class="holder__title">[CEO]</span></p>
      <div class="divider"></div>
      <ul class="contact">
        <li>2180 Larkspur Ave., Fairmont, OR 97015</li>
        <li>dwhitfield@crestlineortho.com</li>
        <li>(555)318-2047</li>
      </ul>
    </div>
  </section>

  <section class="card card--dark">
    <div class="card__face">
      <div class="brand">
        <span class="brand__dot"></span>
        <span class="brand__text">
          <span class="brand__name">CRESTLINE</span>
          <span class="brand__tag">Orthopaedic &amp; Sports</span>
          <span class="brand__sub">Medicine Center</span>
        </span>
      </div>
      <p class="holder">DORIAN WHITFIELD <span class="holder__title">[CEO]</span></p>
      <div class="divider"></div>
      <ul class="contact">
        <li>2180 Larkspur Ave., Fairmont, OR 97015</li>
        <li>dwhitfield@crestlineortho.com</li>
        <li>(555)318-2047</li>
      </ul>
    </div>
  </section>

  <p class="caption">bussiness card. 9 cm x 5,5 cm</p>
</main>
</body>
</html>
```